Advertising company unique advertising platform

we need a logo design for a new company based in Australia Melbourne. We develop innovated advertising platform where consumer can use this platform to get regular discount, as business owner they can use this platform for free advertisement. Payment for this advertisement platform only payable every two weeks, when I generate revenue for their business

Industry/Entity Type

Advertising

Contact Information for Business Card

Dale Morrow | Co-Founder |Managing Director
Suite 318 274 Bramwell Lane Melbourne Vic 3000

ABN 62 914 305 718
Tel: +61 0491 258 307 | Email: dale.morrow@plovintarex.com

Font styles to use
Decorative
Script

Requirements
Must have
• Try few different design and some round corner business card
Should not have
• One round corner business card...try 4 different colour background not only black, make sure two side is designed. Be creative so imagine you are giving this to a client make sure has wow factor, if you can also try one design with engrave like all the logo, words look 3d feel
• The word Advertising Platform use attached file font

```html
<!DOCTYPE html>
<html lang="en">
<head>
<meta charset="utf-8">
<title>Kindlepath Collective – Business Card</title>
<link rel="stylesheet" href="https://fonts.googleapis.com/css2?family=Marcellus&family=Work+Sans:wght@400;500;600&display=swap">
<style>
  :root {
    --backdrop: #3a3a3c;
    --card: #ffffff;
    --ink: #1f1f1f;
    --ink-soft: #555555;
    --orange: #f07a1e;
    --teal: #5fb8a6;
    --rule: #2a2a2a;
  }
  * { margin: 0; padding: 0; box-sizing: border-box; }
  html, body {
    width: 1200px; height: 859px; overflow: hidden;
    background: var(--backdrop);
  }
  .canvas {
    position: relative; width: 1200px; height: 859px;
    display: flex; flex-direction: column; align-items: center; justify-content: center; gap: 40px;
  }
  .card {
    position: relative; width: 620px; height: 354px;
    background: var(--card);
    box-shadow: 0 10px 28px rgba(0,0,0,.45);
  }
  .brand {
    display: flex; align-items: center; gap: 12px;
    font-family: "Work Sans", sans-serif; font-weight: 600;
    color: var(--teal);
  }
  .brand-dot {
    width: 30px; height: 30px; border-radius: 50%; background: var(--orange);
    flex: none;
  }
  .card-front .brand {
    position: absolute; left: 50%; top: 50%; transform: translate(-50%, -50%);
    font-size: 34px; white-space: nowrap;
  }
  .card-front .brand-dot { width: 48px; height: 48px; }
  .card-back .brand {
    position: absolute; right: 36px; top: 42px; font-size: 20px;
  }
  .abn {
    position: absolute; right: 36px; top: 88px;
    font-family: "Work Sans", sans-serif; font-size: 13px; color: var(--ink);
    letter-spacing: .04em;
  }
  .label { color: var(--orange); }
  .rule-top {
    position: absolute; left: 240px; right: 50px; top: 196px;
    height: 1px; background: var(--rule);
  }
  .person {
    position: absolute; left: 36px; top: 206px;
  }
  .person-name {
    font-family: "Marcellus", serif; font-size: 30px; color: var(--orange);
    letter-spacing: .03em; text-transform: uppercase; line-height: 1;
  }
  .person-title {
    font-family: "Marcellus", serif; font-size: 11.5px; color: var(--ink-soft);
    letter-spacing: .06em; text-transform: uppercase; margin-top: 4px;
  }
  .rule-bottom {
    position: absolute; left: 36px; right: 50px; top: 268px;
    height: 1px; background: var(--rule);
  }
  .contact {
    position: absolute; left: 36px; top: 280px;
    font-family: "Work Sans", sans-serif; font-size: 14px; color: var(--ink);
    line-height: 1.55; letter-spacing: .03em;
  }
  .sep { color: var(--orange); margin: 0 8px; }
</style>
</head>
<body>
  <main class="canvas">
    <section class="card card-front" aria-label="Card front">
      <div class="brand"><span class="brand-dot"></span>Kindlepath Collective</div>
    </section>

    <section class="card card-back" aria-label="Card back">
      <div class="brand"><span class="brand-dot"></span>Kindlepath Collective</div>
      <p class="abn"><span class="label">ABN:</span> 62 914 305 718</p>
      <div class="rule-top"></div>
      <div class="person">
        <h1 class="person-name">Dale Morrow</h1>
        <p class="person-title">|Co-Founder | Managing Director</p>
      </div>
      <div class="rule-bottom"></div>
      <div class="contact">
        <p><span class="label">Tel:</span> +61 0491 258 307<span class="sep">|</span>dale.morrow@plovintarex.com</p>
        <p>Suite 318 274 Bramwell Lane Melbourne Vic 3000</p>
      </div>
    </section>
  </main>
</body>
</html>
```